new Outdoor Product company needs a label for brand new product

Brand: Heron Outdoor Products
Item Name: Heron Grips
Picture of alligator
address:Reedport, MS 70512
website URL - heronoutdoorproducts.com
Facebook: www.facebook.com/heronoutdoorproducts
I will be putting labels on the actual product and need a design on the packaging.
I would like a picture of an alligator in the design.
I would like the Writing to be bright yellow
the product is green with a yellow handle

file type: in PSD format
Size: 90*50mm

It Company

```html
<!DOCTYPE html>
<html lang="en">
<head>
<meta charset="utf-8">
<title>Heron Grips – Packaging Label</title>
<link rel="stylesheet" href="https://fonts.googleapis.com/css2?family=Lato:wght@400;700&display=swap">
<style>
  :root {
    --label-green: #86a832;
    --bright-yellow: #fde95e;
    --yellow-soft: #f6e36a;
  }
  html, body {
    margin: 0;
    padding: 0;
    width: 1200px;
    height: 668px;
    overflow: hidden;
    background: var(--label-green);
  }
  .label {
    position: relative;
    width: 1200px;
    height: 668px;
    background: var(--label-green);
    font-family: "Lato", sans-serif;
    color: var(--bright-yellow);
    overflow: hidden;
  }
  .frame-bar {
    position: absolute;
    background: var(--bright-yellow);
  }
  .frame-top    { left: 10px;   top: 22px;  width: 1160px; height: 12px; }
  .frame-bottom { left: 10px;   top: 648px; width: 1160px; height: 12px; }
  .frame-left   { left: 10px;   top: 22px;  width: 14px;   height: 638px; }
  .frame-right-upper { left: 1156px; top: 22px;  width: 14px; height: 272px; }
  .frame-right-lower { left: 1156px; top: 504px; width: 14px; height: 156px; }

  .product-name {
    position: absolute;
    left: 0;
    width: 1200px;
    top: 66px;
    margin: 0;
    text-align: center;
    font-weight: 700;
    font-size: 140px;
    line-height: 1;
    letter-spacing: 2px;
  }
  .alligator-art {
    position: absolute;
    left: 700px;
    top: 234px;
    width: 500px;
    height: 296px;
  }
  .contact {
    position: absolute;
    left: 68px;
    top: 436px;
    margin: 0;
    font-weight: 400;
    font-size: 66px;
    line-height: 88px;
  }
  .contact span { display: block; }
</style>
</head>
<body>
  <main class="label">
    <div class="frame-bar frame-top"></div>
    <div class="frame-bar frame-bottom"></div>
    <div class="frame-bar frame-left"></div>
    <div class="frame-bar frame-right-upper"></div>
    <div class="frame-bar frame-right-lower"></div>

    <h1 class="product-name">HERON GRIPS</h1>

    <svg class="alligator-art" viewBox="0 0 500 296" role="img" aria-label="Yellow silhouette illustration of an alligator with open jaws, facing left">
      <defs>
        <linearGradient id="art-fill" x1="0" y1="0" x2="1" y2="0">
          <stop offset="0" stop-color="#fde95e"/>
          <stop offset="1" stop-color="#f6e36a"/>
        </linearGradient>
      </defs>
      <rect x="0" y="0" width="500" height="296" rx="40" fill="url(#art-fill)"/>
    </svg>

    <p class="contact">
      <span class="address">Reedport, MS 70512</span>
      <span class="website">heronoutdoorproducts.com</span>
    </p>
  </main>
</body>
</html>
```